New Update: I am changing the title of the book and the back cover text. Title was too long before. Same style as before.
New Title: Under the Quiet Sky
New Subtitle: A Gardener’s Notes on Patience (italics on front cover)

Back cover text:
Under the Quiet Sky: A Gardener’s Notes on Patience offers clear, compassionate guidance for those recovering from total loss. Drawing from his experience as a Brennick Flood survivor, Tobias Quellhorst shares practical advice on insurance, rebuilding, and emotional healing, along with lessons in strength and community. This is not a book about tragedy; it’s about perseverance and renewal. Under the Quiet Sky is a trusted companion for anyone rebuilding life, home, and hope after disaster.

Font styles to use
Serif

Colors
EB3D1F
EC4F4E
F09395
F8D3D4
FCEDEE

Requirements
Should not have
• No pictures or anything related to fire on the cover.

```html
<!DOCTYPE html>
<html lang="en">
<head>
<meta charset="utf-8">
<title>Under the Quiet Sky — Cover Wrap</title>
<link rel="stylesheet" href="https://fonts.googleapis.com/css2?family=Arimo:wght@700&family=Playfair+Display:ital,wght@0,700;0,900;1,900&display=swap">
<style>
  :root {
    --ink-white: #ffffff;
    --wine-deep: #2a0607;
    --wine: #5a1211;
    --crimson: #7a1816;
    --ember-red: #b8262a;
    --glow-orange: #f0604a;
    --shadow: #120304;
    --portrait-bg: #e9e8e4;
    --portrait-suit: #2b3650;
  }
  * { margin: 0; padding: 0; box-sizing: border-box; }
  html, body { width: 1200px; height: 865px; overflow: hidden; background: var(--shadow); }

  .cover-wrap {
    position: relative;
    width: 1200px;
    height: 865px;
    overflow: hidden;
    color: var(--ink-white);
    background:
      radial-gradient(ellipse 320px 220px at 10px 40px, rgba(240,96,74,0.95), rgba(240,96,74,0) 100%),
      radial-gradient(ellipse 260px 240px at 1200px 60px, rgba(214,44,44,0.9), rgba(214,44,44,0) 100%),
      radial-gradient(ellipse 380px 160px at 330px 520px, rgba(130,26,24,0.7), rgba(130,26,24,0) 100%),
      radial-gradient(ellipse 420px 200px at 620px 640px, rgba(122,24,22,0.75), rgba(122,24,22,0) 100%),
      radial-gradient(ellipse 360px 260px at 1150px 860px, rgba(10,2,3,0.95), rgba(10,2,3,0) 100%),
      linear-gradient(155deg, var(--crimson) 0%, var(--wine-deep) 22%, var(--crimson) 40%, var(--wine) 55%, var(--wine-deep) 70%, var(--crimson) 82%, var(--shadow) 100%);
  }

  /* Back cover */
  .back-blurb {
    position: absolute;
    left: 84px;
    top: 171px;
    width: 420px;
    font-family: "Arimo", Arial, sans-serif;
    font-weight: 700;
    font-size: 16.4px;
    line-height: 21.7px;
  }
  .back-blurb p + p { margin-top: 10px; }

  .back-rule {
    position: absolute;
    left: 192px;
    top: 464px;
    width: 197px;
    height: 2px;
    background: var(--ink-white);
  }

  .author-portrait {
    position: absolute;
    left: 232px;
    top: 513px;
    width: 120px;
    height: 123px;
    border: 2px solid var(--ink-white);
    background: linear-gradient(180deg, var(--portrait-bg) 0%, var(--portrait-bg) 55%, var(--portrait-suit) 100%);
  }

  .back-author {
    position: absolute;
    left: 191px;
    top: 644px;
    width: 200px;
    text-align: center;
    font-family: "Playfair Display", Georgia, serif;
    font-weight: 700;
    font-size: 12.5px;
    white-space: nowrap;
  }

  .code-panel {
    position: absolute;
    left: 344px;
    top: 718px;
    width: 165px;
    height: 88px;
    background: var(--ink-white);
  }

  /* Spine */
  .spine {
    position: absolute;
    left: 588px;
    top: 0;
    width: 26px;
    height: 865px;
  }
  .spine-text {
    position: absolute;
    left: 0;
    writing-mode: vertical-rl;
    font-family: "Playfair Display", Georgia, serif;
    font-weight: 900;
    font-size: 15.5px;
    line-height: 26px;
    white-space: nowrap;
  }
  .spine-title { top: 262px; }
  .spine-author { top: 470px; }

  /* Front cover */
  .front {
    position: absolute;
    left: 680px;
    top: 0;
    width: 454px;
    height: 865px;
    text-align: center;
  }
  .front-title {
    position: absolute;
    left: 0;
    top: 132px;
    width: 100%;
    font-family: "Playfair Display", Georgia, serif;
    font-weight: 900;
    font-size: 96px;
    line-height: 84px;
    letter-spacing: -1px;
    text-transform: uppercase;
  }
  .front-title span { display: block; }
  .front-subtitle {
    position: absolute;
    left: 0;
    top: 543px;
    width: 100%;
    font-family: "Playfair Display", Georgia, serif;
    font-style: italic;
    font-weight: 900;
    font-size: 34px;
    line-height: 46px;
  }
  .front-author {
    position: absolute;
    left: 0;
    top: 750px;
    width: 100%;
    font-family: "Playfair Display", Georgia, serif;
    font-weight: 700;
    font-size: 33px;
    letter-spacing: -0.5px;
    white-space: nowrap;
  }
</style>
</head>
<body>
  <main class="cover-wrap">
    <section class="back-cover">
      <div class="back-blurb">
        <p>Under the Quiet Sky: A Gardener’s Notes on Patience offers clear, compassionate guidance for those recovering from total loss. Drawing from his experience as a Brennick Flood survivor, Tobias Quellhorst shares practical advice on insurance, rebuilding, and emotional healing, along with lessons in strength and community.</p>
        <p>This is not a book about tragedy; it’s about perseverance and renewal. Under the Quiet Sky is a trusted companion for anyone rebuilding life, home, and hope after disaster.</p>
      </div>
      <div class="back-rule"></div>
      <div class="author-portrait" role="img" aria-label="Author portrait photo of Tobias Quellhorst"></div>
      <div class="back-author">TOBIAS QUELLHORST</div>
      <div class="code-panel"></div>
    </section>

    <section class="spine">
      <div class="spine-text spine-title">UNDER THE QUIET SKY</div>
      <div class="spine-text spine-author">TOBIAS QUELLHORST</div>
    </section>

    <section class="front">
      <h1 class="front-title"><span>Under</span><span>the</span><span>Quiet</span><span>Sky</span></h1>
      <p class="front-subtitle">A Gardener’s Notes on<br>Patience</p>
      <p class="front-author">TOBIAS QUELLHORST</p>
    </section>
  </main>
</body>
</html>
```